Redesigned Website for Investment Firm/Investment Education Company

DO NOT CONTACT PRIVATELY - ALL PRIVATE MESSAGES WILL BE IGNORED

Please avoid complex design techniques. Should be professional and modern with a linear design approach.

Please see uploaded file for existing content

The company is The Birchwell Capital Trust, LLC, and they provide investment education and services. Their Practical Holdings Stewardship academic program offers a two-year analyst program for undergraduate students, combining academic, research, money management, and career components. The company manages $5.5 million in assets and follows the value investing philosophy of Douglas R. Pemberly. The website should have a modern and professional design, with a linear layout that is not too busy.

The website should consist of five pages:

1 Welcome page: This page should have a top image with a (player label omitted) video play button or embedded (player label omitted) video that highlights the company's services and offerings.

Underneath that there should be an overview section of the services offered, with a textual description underneath that highlights the company's services and offerings.

Below the overview section, there should be an "Our Investment Approach" section with a clear and concise description of the company's investment philosophy. This section should describe the company's focus on value investing, and its approach to identifying investment opportunities through intensive research of individual companies.

The page should have a modern and professional design, with a clear overview of the company and its services. It should include some key features that set it apart from its competitors, and a call to action for users to learn more or sign up for their programs.

2 Programs page: This page should emphasize that the classes have a fall, spring, and summer schedule. The page should include a table showing the available classes in each season. The design should be modern and professional, with a focus on making it easy for users to understand the different programs and their benefits.

3 Directors page: This page should provide users with information and bios of the directors of the business. The design should be clean and modern, with each director's photo and a detailed bio.

4 Senior Analysts page: This page should provide users with information and bios of the senior analysts of the business. The design should be clean and modern, with each analyst's photo and a detailed bio.

5 Junior Analysts page: This page should provide users with information and bios of the junior analysts of the business. The design should be clean and modern, with each analyst's photo and a detailed bio.

DO NOT INCLUDE
- search bar
- login buttons

Target Market(s)

Students looking to get into investing

Industry/Entity Type

Finance/Investing

Number of Pages Required

5+ page

Colors
F0912C
F2A743
F7CA91
FBE8D2
FDF5EE

Requirements
Should not have
• - search bar - login buttons

```html
<!DOCTYPE html>
<html lang="en">
<head>
<meta charset="utf-8">
<title>Birchwell Capital Trust</title>
<link href="https://fonts.googleapis.com/css2?family=Roboto:wght@400;500;700&display=swap" rel="stylesheet">
<style>
:root{
  --orange:#F0912C;
  --orange-2:#F2A743;
  --orange-3:#F7CA91;
  --orange-4:#FBE8D2;
  --orange-5:#FDF5EE;
  --ink:#222222;
  --text:#666666;
  --dark:#242424;
  --white:#ffffff;
  --ring:#eeeeee;
}
*{box-sizing:border-box;margin:0;padding:0}
html,body{width:1200px;height:3429px;overflow:hidden}
body{position:relative;font-family:'Roboto',sans-serif;background:var(--white);color:var(--ink)}
.abs{position:absolute}
.hero-bg{left:0;top:0;width:1200px;height:878px;background:linear-gradient(100deg,#ffffff 0%,#f1f3f5 30%,#e4e9ee 55%,#c9d4de 78%,#b7c6d3 100%)}
.hero-fade{left:0;top:620px;width:1200px;height:258px;background:linear-gradient(180deg,rgba(255,255,255,0),#ffffff)}
.brand{left:110px;top:20px;font-size:21px;font-weight:500;letter-spacing:.2px;color:var(--ink)}
.nav{top:28px;font-size:12.5px;font-weight:500;color:var(--ink)}
.nav a{position:absolute;white-space:nowrap;color:inherit;text-decoration:none}
.nav a.active{color:var(--orange);border-bottom:2px solid var(--orange);padding-bottom:5px}
.btn-signup{left:990px;top:16px;width:98px;height:39px;background:var(--orange);color:var(--white);font-size:14px;font-weight:500;display:flex;align-items:center;justify-content:center}
.hero-title{left:0;width:1200px;top:122px;text-align:center;font-size:51px;font-weight:700;color:var(--ink)}
.video{left:194px;top:218px;width:812px;height:470px;overflow:hidden}
.video-frame{position:absolute;inset:0;background:linear-gradient(90deg,#c9ccd0 0%,#9fa4aa 30%,#6a7785 34%,#8aa0b8 70%,#4d5e73 100%)}
.video-bar{position:absolute;left:0;right:0;bottom:0;height:48px;background:linear-gradient(180deg,#9b1c1c,#b3201f)}
.video-track{position:absolute;left:28px;right:28px;bottom:50px;height:3px;background:rgba(255,255,255,.4)}
.video-track span{display:block;width:30%;height:100%;background:#d92020}
.video-time{position:absolute;left:104px;bottom:15px;color:#fff;font-size:13px}
.down{left:563px;top:735px;width:74px;height:74px;border-radius:50%;background:#fff;box-shadow:0 2px 10px rgba(0,0,0,.08);display:flex;align-items:center;justify-content:center}
.accent{background:var(--orange)}
.photo{background:linear-gradient(135deg,#8a7a6c,#c9b9a7 55%,#6e7f93)}
.h2{font-size:40px;font-weight:700;color:var(--ink)}
.para{font-size:14px;line-height:26px;color:var(--text);text-align:justify}
.btn{height:40px;font-size:14px;font-weight:700;display:flex;align-items:center;justify-content:center;gap:4px}
.btn-orange{background:var(--orange);color:#fff}
.btn-white{background:#fff;color:var(--orange)}
.band{left:0;top:1515px;width:1200px;height:459px;background:var(--orange)}
.family{left:621px;top:1462px;width:467px;height:565px;background:linear-gradient(150deg,#c5ad92,#e8ddd0 50%,#a48566)}
.section-title{left:0;width:1200px;text-align:center;font-size:35px;font-weight:700;color:var(--ink)}
.feature{width:220px;text-align:center}
.feature svg{display:block;margin:0 auto}
.feature h3{font-size:18px;font-weight:500;color:var(--ink);margin-top:10px}
.feature p{font-size:13.5px;line-height:26px;color:var(--text);margin-top:6px}
.signup-text{left:300px;width:600px;top:2720px;text-align:center;font-size:14px;line-height:26px;color:var(--text)}
.signup-form{left:311px;top:2790px;width:578px;height:62px;border:1px solid #ddd;border-radius:3px}
.signup-form .field{position:absolute;left:30px;top:22px;font-size:14px;color:#666}
.signup-form .btn{position:absolute;left:440px;top:11px;width:126px;height:40px;border-radius:2px}
.footer-title{left:0;width:1200px;top:3138px;text-align:center;font-size:24px;font-weight:500;color:#fff}
.footer-nav{left:0;width:1200px;top:3200px;display:flex;justify-content:center;gap:22px;font-size:12.5px;font-weight:700;color:#fff}
.contact{display:flex;gap:14px;color:#fff;font-size:12.5px;line-height:21px}
.contact .ico{width:38px;height:38px;border-radius:50%;background:#3d3d3d;display:flex;align-items:center;justify-content:center;flex:none;margin-top:3px}
.contact b{font-weight:700}
.copyright{left:0;width:1200px;top:3366px;text-align:center;font-size:14px;color:#fff}
</style>
</head>
<body>

<header>
  <div class="abs hero-bg" role="img" aria-label="Upward view of a glass office tower"></div>
  <div class="abs hero-fade"></div>
  <div class="abs brand">BIRCHWELL CAPITAL TRUST</div>
  <nav class="abs nav" style="left:0;width:1200px">
    <a class="active" style="left:470px">HOME</a>
    <a style="left:528px">PROGRAMS</a>
    <a style="left:621px">DIRECTORS</a>
    <a style="left:712px">SENIOR ANALYSTS</a>
    <a style="left:847px">JUNIOR ANALYSTS</a>
  </nav>
  <div class="abs btn-signup">SIGN UP</div>
  <h1 class="abs hero-title">BIRCHWELL CAPITAL TRUST</h1>
  <div class="abs video">
    <div class="video-frame" role="img" aria-label="Video still of the fund's director speaking in an office beside a world map graphic"></div>
    <div class="video-track"><span></span></div>
    <div class="video-bar">
      <svg class="abs" style="left:28px;top:14px" width="20" height="20" viewBox="0 0 20 20"><path d="M3 1 L18 10 L3 19 Z" fill="#fff"/></svg>
      <svg class="abs" style="left:62px;top:14px" width="22" height="20" viewBox="0 0 22 20"><path d="M2 7 H6 L11 3 V17 L6 13 H2 Z" fill="#fff"/><path d="M14 6 Q17 10 14 14 M16.5 3.5 Q21 10 16.5 16.5" stroke="#fff" stroke-width="1.6" fill="none"/></svg>
      <div class="video-time">1.28&nbsp;&nbsp;/&nbsp;&nbsp;14.11</div>
      <svg class="abs" style="left:634px;top:14px" width="20" height="20" viewBox="0 0 20 20"><circle cx="10" cy="10" r="6" fill="none" stroke="#fff" stroke-width="4" stroke-dasharray="3 2.2"/><circle cx="10" cy="10" r="2.5" fill="#fff"/></svg>
      <svg class="abs" style="left:767px;top:14px" width="20" height="20" viewBox="0 0 20 20" fill="none" stroke="#fff" stroke-width="2.4"><path d="M2 7V2H7M13 2H18V7M18 13V18H13M7 18H2V13"/></svg>
    </div>
  </div>
  <div class="abs down"><svg width="26" height="36" viewBox="0 0 26 36" fill="none" stroke="#111" stroke-width="2.4"><path d="M13 2V33M3 23L13 33L23 23"/></svg></div>
</header>

<section class="overview">
  <div class="abs accent" style="left:110px;top:930px;width:136px;height:138px"></div>
  <div class="abs accent" style="left:411px;top:1236px;width:134px;height:137px"></div>
  <div class="abs photo" style="left:138px;top:954px;width:393px;height:403px" role="img" aria-label="Young analyst reviewing a document at a laptop"></div>
  <h2 class="abs h2" style="left:600px;top:946px">COMPANY OVERVIEW</h2>
  <p class="abs para" style="left:600px;top:1012px;width:488px">Lorem ipsum dolor sit amet, consectetur adipiscing elit, sed do eiusmod tempor incididunt ut labore et dolore magna aliqua. Ut enim ad minim veniam, quis nostrud exercitation ullamco laboris nisi ut aliquip ex ea commodo consequat. Duis aute irure dolor in reprehenderit in voluptate velit esse cillum dolore eu fugiat nulla pariatur.</p>
  <p class="abs para" style="left:600px;top:1166px;width:488px">Excepteur sint occaecat cupidatat non proident, sunt in culpa qui officia deserunt mollit anim id est laborum. Lorem ipsum dolor sit amet, consectetur adipiscing elit, sed do eiusmod tempor incididunt ut labore et dolore magna aliqua. Ut enim ad minim veniam, quis nostrud exercitation ullamco laboris nisi ut aliquip ex ea commodo consequat.</p>
  <div class="abs btn btn-orange" style="left:600px;top:1317px;width:150px">LEARN MORE <svg width="13" height="13" viewBox="0 0 14 14"><circle cx="7" cy="7" r="7" fill="#fff"/><path d="M5.5 4L8.5 7L5.5 10" stroke="#F0912C" stroke-width="2" fill="none"/></svg></div>
</section>

<section class="approach">
  <div class="abs band"></div>
  <div class="abs family" role="img" aria-label="Family saving coins in a piggy bank together"></div>
  <h2 class="abs h2" style="left:110px;top:1580px;color:#fff;font-size:36px">OUR INVESTMENT APPROACH</h2>
  <p class="abs para" style="left:112px;top:1639px;width:488px;color:#fff">Lorem ipsum dolor sit amet, consectetur adipiscing elit, sed do eiusmod tempor incididunt ut labore et dolore magna aliqua. Ut enim ad minim veniam, quis nostrud exercitation ullamco laboris nisi ut aliquip ex ea commodo consequat. Duis aute irure dolor in reprehenderit in voluptate velit esse cillum dolore eu fugiat nulla pariatur. Excepteur sint occaecat cupidatat non proident, sunt in culpa qui officia deserunt mollit anim id est laborum. Lorem ipsum dolor sit amet, consectetur adipiscing elit, sed do eiusmod tempor incididunt ut labore et dolore magna aliqua.</p>
  <div class="abs btn btn-white" style="left:112px;top:1867px;width:149px">LEARN MORE <svg width="13" height="13" viewBox="0 0 14 14"><circle cx="7" cy="7" r="7" fill="#F0912C"/><path d="M5.5 4L8.5 7L5.5 10" stroke="#fff" stroke-width="2" fill="none"/></svg></div>
</section>

<section class="features">
  <h2 class="abs section-title" style="top:2137px">KEY FEATURES</h2>

  <div class="abs feature" style="left:121px;top:2214px">
    <svg width="150" height="150" viewBox="0 0 150 150"><circle cx="75" cy="75" r="71" fill="none" stroke="var(--ring)" stroke-width="4"/><circle cx="75" cy="75" r="71" fill="none" stroke="var(--orange)" stroke-width="5" stroke-dasharray="190 500" transform="rotate(-90 75 75)"/><circle cx="75" cy="75" r="54" fill="#f4f4f4"/><g fill="none" stroke="var(--orange)" stroke-width="2"><circle cx="77" cy="66" r="12"/><path d="M77 59V73M81 62H75Q73 62 73 64.5Q73 67 77 67Q81 67 81 69.5Q81 72 78 72H73"/><path d="M52 86H62L74 90H86L100 82Q104 82 102 86L88 96H60M52 82V98"/><path d="M77 42V48M70 44V48M84 44V48"/></g></svg>
    <h3>DUIS AUTE IRURE</h3>
    <p>Lorem ipsum dolor sit amet, consectetur adipiscing elit, sed do eiusmod tempor</p>
  </div>

  <div class="abs feature" style="left:366px;top:2274px">
    <svg width="150" height="150" viewBox="0 0 150 150"><circle cx="75" cy="75" r="71" fill="none" stroke="var(--ring)" stroke-width="4"/><circle cx="75" cy="75" r="71" fill="none" stroke="var(--orange)" stroke-width="5" stroke-dasharray="225 500" transform="rotate(-90 75 75)"/><circle cx="75" cy="75" r="54" fill="#f4f4f4"/><g fill="none" stroke="var(--orange)" stroke-width="2"><path d="M56 45H88L96 53V104H56Z"/><path d="M62 104V86M70 104V80M78 104V84M86 104V76M60 78L70 70L78 74L90 64"/><circle cx="67" cy="56" r="6"/></g></svg>
    <h3>DUIS AUTE IRURE</h3>
    <p>Lorem ipsum dolor sit amet, consectetur adipiscing elit, sed do eiusmod tempor</p>
  </div>

  <div class="abs feature" style="left:611px;top:2214px">
    <svg width="150" height="150" viewBox="0 0 150 150"><circle cx="75" cy="75" r="71" fill="none" stroke="var(--ring)" stroke-width="4"/><circle cx="75" cy="75" r="71" fill="none" stroke="var(--orange)" stroke-width="5" stroke-dasharray="190 500" transform="rotate(-90 75 75)"/><circle cx="75" cy="75" r="54" fill="#f4f4f4"/><g fill="none" stroke="var(--orange)" stroke-width="2"><circle cx="75" cy="56" r="11"/><path d="M75 50V62M75 67V100M75 84Q62 84 58 72Q70 72 75 84M75 84Q88 84 92 72Q80 72 75 84M54 100H96M60 40V54M56 44L60 40L64 44M90 40V54M86 44L90 40L94 44"/></g></svg>
    <h3>DUIS AUTE IRURE</h3>
    <p>Lorem ipsum dolor sit amet, consectetur adipiscing elit, sed do eiusmod tempor</p>
  </div>

  <div class="abs feature" style="left:857px;top:2274px">
    <svg width="150" height="150" viewBox="0 0 150 150"><circle cx="75" cy="75" r="71" fill="none" stroke="var(--ring)" stroke-width="4"/><circle cx="75" cy="75" r="71" fill="none" stroke="var(--orange)" stroke-width="5" stroke-dasharray="225 500" transform="rotate(-90 75 75)"/><circle cx="75" cy="75" r="54" fill="#f4f4f4"/><g fill="none" stroke="var(--orange)" stroke-width="2"><path d="M66 90Q66 82 60 76Q56 70 58 63Q62 52 75 52Q88 52 92 63Q94 70 90 76Q84 82 84 90Z"/><path d="M67 95H83M69 100H81M67 70L73 76L84 64M75 40V46M56 48L60 52M94 48L90 52M48 68H53M97 68H102"/></g></svg>
    <h3>DUIS AUTE IRURE</h3>
    <p>Lorem ipsum dolor sit amet, consectetur adipiscing elit, sed do eiusmod tempor</p>
  </div>
</section>

<section class="signup">
  <h2 class="abs section-title" style="top:2669px">SIGN UP FOR OUR PROGRAMS</h2>
  <p class="abs signup-text">Lorem ipsum dolor sit amet, consectetur adipiscing elit, sed do eiusmod tempor incididunt ut labore et dolore magna aliqua.</p>
  <div class="abs signup-form">
    <span class="field">Email address</span>
    <div class="btn btn-orange">SIGNUP</div>
  </div>
</section>

<footer>
  <svg class="abs" style="left:0;top:2920px" width="1200" height="509" viewBox="0 0 1200 509">
    <polygon points="0,240 412,3 1200,237 1200,252 412,50 0,250" fill="var(--orange)"/>
    <polygon points="0,262 412,62 1200,258 1200,509 0,509" fill="var(--dark)"/>
  </svg>
  <div class="abs footer-title">BIRCHWELL CAPITAL TRUST</div>
  <nav class="abs footer-nav">
    <span>HOME</span><span>|</span><span>PROGRAMS</span><span>|</span><span>DIRECTORS</span><span>|</span><span>SENIOR ANALYSTS</span><span>|</span><span>JUNIOR ANALYSTS</span>
  </nav>
  <div class="abs contact" style="left:201px;top:3262px">
    <div class="ico"><svg width="14" height="16" viewBox="0 0 14 18"><path d="M7 1C3.5 1 1 3.5 1 7C1 11 7 17 7 17C7 17 13 11 13 7C13 3.5 10.5 1 7 1Z" fill="#fff"/><circle cx="7" cy="7" r="2.2" fill="#3d3d3d"/></svg></div>
    <div><b>Managing Director</b><br>The Douglas R. Pemberly<br>Professor of Finance</div>
  </div>
  <div class="abs contact" style="left:501px;top:3262px">
    <div class="ico"><svg width="14" height="14" viewBox="0 0 16 16"><path d="M3 1L6 1L7 5L5 6.5Q6.5 9.5 9.5 11L11 9L15 10V13Q15 15 13 15Q1 14 1 3Q1 1 3 1Z" fill="#fff"/></svg></div>
    <div><b>Phone</b><br>315 555 0182</div>
  </div>
  <div class="abs contact" style="left:734px;top:3262px">
    <div class="ico"><svg width="14" height="11" viewBox="0 0 16 12"><rect x="0" y="0" width="16" height="12" rx="1" fill="#fff"/><path d="M1 1L8 7L15 1" stroke="#3d3d3d" stroke-width="1.4" fill="none"/></svg></div>
    <div><b>Email</b><br>GeraldAshcombe@BirchwellCapital.com</div>
  </div>
  <div class="abs copyright">Copyright © 2023 | Birchwell Capital Trust</div>
</footer>

</body>
</html>
```